Ovelin Watch app inspired by the Perch Thermostat

Wendle allows you to control your Perch Thermostat from your Ovelin Orbit device (Zentrix Watch).
The UI consists of two screens, phone and device, and the design will resemble the Perch look and feel (do not exactly copy, I need something that looks similar). The thermostat control will be front and center, with a white background and blue highlights.
A logo is also needed (custom typography is a plus).

My app is live in the Ovelin Bazaar Market at:
shop.zentrix.example/store/apps/details?id=com.brightforgeworks.wendle

The app currently supports the following devices:

The KV Qband:
https://shop.zentrix.example/store/devices/details?id=kv_q_band_black

The Tarvolo Rook Pulse:
https://shop.zentrix.example/store/devices/details?id=tarvolo_rook_pulse_black

Target Market(s)

Zentrix Watch wearers who have a Perch at home.

Industry/Entity Type

Ovelin

Colors
33a6d7
0555a3
3176b5
fefefe
85acd3
ffffff
cee9f5
cedeec
fbc994

Requirements
Must have
• Two screen designs:
• 1. A 1080 x 1920 px layout for ovelin phones.
• 2. A 320 x 320 px layout for Ovelin Orbit devices (please Zentrix "KV Q Band" or "Tarvolo Rook Pulse" for a visual of the devices I support).
• Design should resemble the Perch experience at perch.example. Using similar fonts, theme and shapes is a must. Please don't copy and paste elements. I need your interpretation of the UI, not the exact same elements from Perch.
• Please look at the screenshots of the Perch Ovelin app for inspiration:
• https://shop.zentrix.example/store/apps/details?id=com.perchworks.ovelin&hl=en
Nice to have
• The project consists of two rather simple layouts, so I'm asking for a logo for my app as well.
Should not have
• No black/dark backgrounds, no square buttons. Please approach the Perch look and feel as much as possible, especially in the QBand design.
• This should go without saying but:
• DO NOT copy paste elements from the Perch page. DO NOT plagiarize other peoples logos or artwork.
• Only original design work will win the contest.

```html
<!DOCTYPE html>
<html lang="en">
<head>
<meta charset="utf-8">
<title>Wendle — Phone Screen</title>
<link rel="stylesheet" href="https://fonts.googleapis.com/css2?family=Nunito:wght@800&family=Roboto:wght@400;500;700&display=swap">
<style>
  :root {
    --backdrop: #e6e3df;
    --status-bar: #000000;
    --app-bar: #25252b;
    --app-title: #ffffff;
    --menu-dots: #9a9a9e;
    --status-icon: #33a6d7;
    --screen: #ffffff;
    --label-grey: #6b6b6b;
    --dial-edge: #2c6fc2;
    --dial-light: #5aa0e6;
    --dial-deep: #2b6cc7;
    --dial-text: #ffffff;
    --dial-target: #cedeec;
    --chevron: rgba(206, 222, 236, 0.45);
  }
  * { margin: 0; padding: 0; box-sizing: border-box; }
  html, body { width: 1200px; height: 900px; overflow: hidden; }
  body { background: var(--backdrop); position: relative; font-family: "Roboto", sans-serif; }

  .phone-screen {
    position: absolute; left: 350px; top: 0; width: 500px; height: 900px;
    background: var(--screen); overflow: hidden;
  }
  .status-bar {
    height: 38px; background: var(--status-bar);
    display: flex; justify-content: flex-end; align-items: center; gap: 6px;
    padding-right: 10px; color: var(--status-icon); font-size: 19px;
  }
  .status-bar svg { display: block; }
  .app-bar {
    height: 77px; background: var(--app-bar);
    display: flex; align-items: center; justify-content: space-between;
    padding: 0 30px 0 20px;
  }
  .app-title {
    font-family: "Nunito", sans-serif; font-weight: 800; font-size: 31px;
    color: var(--app-title); letter-spacing: 0.3px;
  }
  .overflow-menu { display: flex; flex-direction: column; gap: 5px; }
  .overflow-menu span { width: 9px; height: 9px; background: var(--menu-dots); display: block; }

  .room-header { text-align: center; color: var(--label-grey); font-weight: 500; margin-top: 15px; }
  .room-name { font-size: 31px; line-height: 36px; }
  .room-status { font-size: 26px; line-height: 32px; }

  .thermostat-dial { position: absolute; left: 70px; top: 270px; width: 370px; height: 370px; }
  .dial-mode, .dial-current, .dial-target { position: absolute; color: var(--dial-text); font-weight: 700; }
  .dial-mode { left: 0; width: 370px; text-align: center; top: 112px; font-size: 26px; letter-spacing: 0.2px; }
  .dial-current { left: 106px; top: 135px; font-size: 108px; line-height: 120px; letter-spacing: -2px; }
  .dial-target { left: 244px; top: 172px; font-size: 42px; line-height: 48px; color: var(--dial-target); }
</style>
</head>
<body>
<main class="phone-screen">
  <div class="status-bar">
    <svg width="22" height="18" viewBox="0 0 22 18" aria-hidden="true">
      <path d="M11 17 L0 5 A16 16 0 0 1 22 5 Z" fill="currentColor"/>
    </svg>
    <svg width="14" height="18" viewBox="0 0 14 18" aria-hidden="true">
      <path d="M0 18 L14 0 L14 18 Z" fill="currentColor"/>
    </svg>
    <svg width="11" height="20" viewBox="0 0 11 20" aria-hidden="true">
      <rect x="3" y="0" width="5" height="3" fill="currentColor"/>
      <rect x="0" y="2" width="11" height="18" rx="1" fill="currentColor"/>
    </svg>
    <span class="status-time">7:07</span>
  </div>

  <header class="app-bar">
    <h1 class="app-title">Wendle</h1>
    <div class="overflow-menu" aria-label="More options"><span></span><span></span><span></span></div>
  </header>

  <section class="room-header">
    <p class="room-name">Living Room</p>
    <p class="room-status">Online</p>
  </section>

  <div class="thermostat-dial">
    <svg width="370" height="370" viewBox="0 0 370 370" aria-hidden="true">
      <defs>
        <linearGradient id="dialFace" x1="0" y1="0" x2="1" y2="1">
          <stop offset="0" stop-color="var(--dial-light)"/>
          <stop offset="1" stop-color="var(--dial-deep)"/>
        </linearGradient>
        <mask id="tickGap">
          <rect width="370" height="370" fill="#fff"/>
          <polygon points="185,185 40,390 185,420 330,390" fill="#000"/>
        </mask>
      </defs>
      <circle cx="185" cy="185" r="184" fill="var(--dial-edge)"/>
      <circle cx="185" cy="185" r="178" fill="url(#dialFace)"/>
      <circle cx="185" cy="185" r="162" fill="none" stroke="#ffffff" stroke-opacity="0.9"
              stroke-width="22" stroke-dasharray="1.3 5.75" mask="url(#tickGap)"/>
      <line x1="136" y1="36" x2="131" y2="52" stroke="#ffffff" stroke-width="5" stroke-linecap="round"/>
      <line x1="277" y1="47" x2="266" y2="63" stroke="#ffffff" stroke-width="5" stroke-linecap="round"/>
      <polyline points="161,88 185,66 209,88" fill="none" stroke="var(--chevron)" stroke-width="7"/>
      <polyline points="161,288 185,310 209,288" fill="none" stroke="var(--chevron)" stroke-width="7"/>
    </svg>
    <p class="dial-mode">HEATING</p>
    <p class="dial-current">72</p>
    <p class="dial-target">78</p>
  </div>
</main>
</body>
</html>
```